Velcrest-Aura

Letter heads, business cards, packaging envelopes big and small, and stationery
We have logo design and trademarked approval, we would lie to
upload design to help create this project.
This product was created for my Mother a 4 time diganosed Cancer
Survivor, This product has patent pending and now will be offered to the general public as well.
We are looking foward to working with all of you as this product
and stationary will be viewed worldwide.
Thanks
The Kindale Family

Target Market(s)

all ages and worldwide

Industry/Entity Type

Business

Requirements
Must have
• Our Logo

```html
<!DOCTYPE html>
<html lang="en">
<head>
<meta charset="utf-8">
<title>Velcrest-Aura Stationery</title>
<link rel="stylesheet" href="https://fonts.googleapis.com/css2?family=Arimo:wght@400;700&family=Open+Sans:wght@400;700&display=swap">
<style>
:root{
  --bg:#e8e5e0;
  --paper:#ffffff;
  --red:#b3000b;
  --navy:#1b3e7d;
  --ink:#1a1a1a;
  --muted:#333333;
  --faint:#ececec;
}
*{margin:0;padding:0;box-sizing:border-box}
html,body{width:1200px;height:1000px;overflow:hidden}
body{background:var(--bg);font-family:"Arimo",Arial,sans-serif;color:var(--ink);position:relative}
.sheet{position:absolute;background:var(--paper);box-shadow:0 2px 6px rgba(0,0,0,.18);overflow:hidden}
.brand{position:absolute;display:flex;align-items:center;gap:6px;font-family:"Arimo",Arial,sans-serif;font-weight:700;color:var(--navy);white-space:nowrap}
.brand .dot{border-radius:50%;background:var(--red);flex:none}
.contact{position:absolute;font-size:8.4px;line-height:11.5px;color:var(--muted)}
.contact b{color:var(--red);font-weight:400}
.edge-bar{position:absolute;background:var(--navy);width:4px}
.faint-mark{position:absolute;border-radius:50%;background:var(--faint)}

/* letterhead */
.letterhead{left:24px;top:51px;width:568px;height:736px}
.letterhead .brand{left:36px;top:30px;font-size:21px}
.letterhead .brand .dot{width:14px;height:14px}
.letterhead .contact{left:369px;top:24px}
.letterhead .edge-bar{right:4px;top:22px;height:48px}
.letter-body{position:absolute;left:63px;top:145px;width:460px;font-size:9.3px;line-height:12.8px}
.letter-body .greeting{margin-bottom:4px}
.letter-body p{margin-left:40px;margin-bottom:13px}
.letterhead .faint-mark{left:365px;top:440px;width:180px;height:180px}
.signature{position:absolute;left:40px;top:590px;width:120px;height:28px;background:linear-gradient(90deg,#d8d8d8,#eeeeee)}
.signer{position:absolute;left:75px;top:624px;font-size:8.5px}

/* red business card */
.card-front{left:633px;top:13px;width:384px;height:214px;background:var(--red)}
.card-front .brand{left:20px;top:52px;font-size:28px;color:#ffffff}
.card-front .brand .dot{width:18px;height:18px;background:#ffffff}
.card-front .faint-mark{left:200px;top:40px;width:180px;height:180px;background:rgba(255,255,255,.1)}

/* white business card */
.card-back{left:633px;top:237px;width:384px;height:216px}
.card-back .brand{left:22px;top:32px;font-size:21px}
.card-back .brand .dot{width:14px;height:14px}
.card-title{position:absolute;right:28px;top:103px;text-align:left;font-family:"Open Sans",Arial,sans-serif;color:var(--navy)}
.card-title .name{font-size:22px;font-weight:700;line-height:24px}
.card-title .role{font-size:10.5px;margin-left:52px}
.card-back .edge-bar{right:0;top:100px;height:44px}
.card-back .contact{left:15px;top:146px}

/* envelope back */
.envelope-back{left:609px;top:467px;width:578px;height:249px}
.envelope-back svg{position:absolute;left:0;top:0}

/* envelope front */
.envelope-front{left:609px;top:733px;width:578px;height:254px}
.envelope-front .brand{left:14px;top:26px;font-size:17px}
.envelope-front .brand .dot{width:11px;height:11px}
.envelope-front .faint-mark{left:470px;top:110px;width:95px;height:95px}
.envelope-front .edge-bar{left:0;top:196px;height:46px}
.envelope-front .contact{left:12px;top:197px}
</style>
</head>
<body>

<section class="sheet letterhead">
  <div class="brand"><span class="dot"></span>Velcrest-Aura</div>
  <div class="contact">
    <div><b>a:</b> 5345 Any Street west,Townsvile,ST 54321</div>
    <div><b>p:</b> 000 000 000 &nbsp;<b>f:</b> 000 000 000</div>
    <div><b>e:</b> name@velcrestaura.com</div>
    <div><b>w:</b> www.velcrestaura.com</div>
  </div>
  <div class="edge-bar"></div>
  <div class="faint-mark"></div>
  <div class="letter-body">
    <div class="greeting">Dear Sir / Madam,</div>
    <p>Lorem ipsum dolor sit amet, consectetur adipisicing elit, sed do eiusmod tempor labore et olore magna aliqua. Ut enim ad minim veniam, quis nostrud exercitation ullamco laboris nisi ut aliquip ex ea commodo consequa.Lorem ipsum dolor sit amet, nsectetur adipisicing elit, sed do eiusmod tempor incididunt ut labore et dolore magna aliqua. Ut enim ad minim veniam, quis.</p>
    <p>Lorem ipsum dolor sit amet, consectetur adipisicing elit, sed do eiusmod tempor labore et dolore magna aliqua. Ut enim ad minim veniam, quis nostrud exercitation ullamco laboris nisi ut aliquip ex ea commodo consequa.Lorem ipsum dolor sit amet, nsectetur adipisicing elit, sed do eiusmod tempor incididunt ut labore et dolore magna aliqua. Ut enim ad minim veniam, quis.</p>
    <p>Lorem ipsum dolor sit amet, consectetur adipisicing elit, sed do eiusmod tempor labore et dolore magna aliqua. Ut enim ad minim veniam, quis nostrud exercitation ullamco laboris nisi ut aliquip ex ea commodo consequa.Lorem ipsum dolor sit amet, nsectetur adipisicing elit, sed do eiusmod tempor incididunt ut labore et dolore magna aliqua. Ut enim ad minim veniam, quis.</p>
    <p>Lorem ipsum dolor sit amet, consectetur adipisicing elit, sed do eiusmod tempor labore et dolore magna aliqua. Ut enim ad minim veniam, quis nostrud exercitation ullamco laboris nisi ut aliquip ex ea commodo consequa.Lorem ipsum dolor sit amet, nsectetur adipisicing elit, sed do eiusmod tempor incididunt ut labore et dolore magna aliqua. Ut enim ad minim veniam, quis.</p>
    <p>Lorem ipsum dolor sit amet, consectetur adipisicing elit, sed do eiusmod tempor labore et dolore magna aliqua. Ut enim ad minim veniam, quis nostrud exercitation ullamco laboris nisi ut aliquip ex ea commodo consequa.Lorem ipsum dolor sit amet, nsectetur adipisicing elit, sed do eiusmod tempor incididunt ut labore et dolore magna aliqua. Ut enim ad minim veniam, quis.</p>
  </div>
  <div class="signature" role="img" aria-label="Handwritten signature"></div>
  <div class="signer">Company Director</div>
</section>

<section class="sheet card-front">
  <div class="faint-mark"></div>
  <div class="brand"><span class="dot"></span>Velcrest-Aura</div>
</section>

<section class="sheet card-back">
  <div class="brand"><span class="dot"></span>Velcrest-Aura</div>
  <div class="card-title">
    <div class="name">Name</div>
    <div class="role">Director</div>
  </div>
  <div class="edge-bar"></div>
  <div class="contact">
    <div><b>a:</b> 5345 Any Street west,Townsvile,ST &nbsp;54321</div>
    <div><b>p:</b> 000 000 000 &nbsp;<b>f:</b> 000 000 000</div>
    <div><b>m:</b> 000 000 000</div>
    <div><b>e:</b> name@velcrestaura.com</div>
    <div><b>w:</b> www.velcrestaura.com</div>
  </div>
</section>

<section class="sheet envelope-back">
  <svg width="578" height="249" viewBox="0 0 578 249" aria-hidden="true">
    <path d="M0 0 H578 Q560 20 520 30 L330 88 Q289 100 248 88 L58 30 Q18 20 0 0 Z" fill="var(--red)"/>
  </svg>
</section>

<section class="sheet envelope-front">
  <div class="brand"><span class="dot"></span>Velcrest-Aura</div>
  <div class="faint-mark"></div>
  <div class="edge-bar"></div>
  <div class="contact">
    <div><b>a:</b> 5345 Any Street west,Townsvile,ST 54321</div>
    <div><b>p:</b> 000 000 000 &nbsp;<b>f:</b> 000 000 000</div>
    <div><b>e:</b> name@velcrestaura.com</div>
    <div><b>w:</b> www.velcrestaura.com</div>
  </div>
</section>

</body>
</html>
```